2 Page Simple Modern Flyer for Upholstery Company!

I need a 2 sided printed flyer designed to showcase our company, Larkfield Upholstery. We specialize in custom Upholstery work on booths, banquettes, chairs, etc for restaurants, bars, cafes, medical clinics, schools, condo towers, etc. I need the flyer to combine a brief description and history of the company, the logo, address & contact info as well as several provided project photos with a title of that job and company. Finally I need to have a some sort of list to show the different clients we have worked with.
Those clients include:
Dunmore Hall
The Silver Meadow Gaming Hall
Tovins
Harbin Crust
QWUK
Fennel Room
Corner Hanks
Birch & Vale
Northgate Plaza
Kestrel Ridge College
Sorano
And Many more.
This is the brief description of the company needed:
Larkfield Upholstery has been serving North America for over 60 years. The company began as a family owned and operated business and has grown into a complete manufacturing facility. We can carry your vision straight through the manufacturing process, from initial drawings to finished product, including foam, fabric, framework, and associated millwork. Our 25,000 square foot facility has computer controlled cutters for both fabric and wood cutting capabilities. We have the capacity to take an original design and create products to meet your specifications, or adapt our standardized designs to fit your vision. We have a library of standard configurations that are customizable to meet almost any requirements.
The Contact info that needs to be included:
780-555-0147
www.larkfieldupholstery.example
4812 Pemberly Rd. Edmonton, AB. T0X 9Z9
I will include the logo image and the several other photos that I would like to be used. One of the photos (the silver meadow gaming hall) I would like used in a bigger capacity.
I would like the look to be clean, simple and modern, but also incorporate some depth of a perhaps a few different shades of blues, greys, blacks and whites, similar to the logo design. I will attach a few photo examples of design I liked.
Let me know immediately if you have any questions or need any references.
Thanks.
Target Market(s)
Designers, Architects, Builders, Contractors, Business Owners.
Industry/Entity Type
It Company
Requirements
Must have
- A simple modern design. Possibly using different geometric shapes (traingles, diamonds, squares, rectangles, etc) similar to the examples provided.
- Different Shades of blue, grey and black as the color themes.
- -The provided company description
- -The provided contact info
- -The logo provided
Nice to have
- The logo improved and turned into a separate vector file for future use would be a major plus.
- Some sort of leather looking fabric (grey, dark grey or some shade of blue) as a background to show more of an upholstery look if possible.
- -Use of all 13 provided photos if possible.
- -Logos of all the clients we have worked with.
Should not have
- Too Busy
- Too cluttered

```html
<!DOCTYPE html>
<html lang="en">
<head>
<meta charset="utf-8">
<title>Larkfield Upholstery – Two Page Flyer</title>
<link href="https://fonts.googleapis.com/css2?family=Exo+2:wght@400;600;700&family=PT+Sans:wght@400;700&display=swap" rel="stylesheet">
<style>
  :root{
    --stage:#dcdfe3;
    --navy-deep:#070f1e;
    --navy:#0f1d35;
    --navy-mid:#16294a;
    --blue:#1a8fd8;
    --blue-bright:#2aa4ee;
    --white:#ffffff;
    --grey-bar:#4b4e53;
    --text-soft:#d7dde6;
  }
  *{box-sizing:border-box;margin:0;padding:0}
  html,body{width:1200px;height:1200px;overflow:hidden;background:var(--stage)}
  .stage{position:relative;width:1200px;height:1200px}
  .page{position:absolute;top:217px;width:540px;height:765px;overflow:hidden;
    background:linear-gradient(180deg,var(--navy-mid) 0%,var(--navy) 55%,var(--navy-deep) 100%);
    box-shadow:0 3px 10px rgba(0,0,0,.25);font-family:"PT Sans",sans-serif;color:var(--white)}
  .page--front{left:45px}
  .page--back{left:614px}
  .page svg.art{position:absolute;left:0;top:0}

  .brand{position:absolute;text-align:left;font-family:"Exo 2",sans-serif;font-weight:700;color:var(--white);line-height:1}
  .brand__name{display:block;font-size:44px;letter-spacing:-1px}
  .brand__sub{display:block;font-size:12px;letter-spacing:5px;margin-top:6px;padding-left:4px}
  .page--front .brand{left:292px;top:548px}
  .page--back .brand{left:30px;top:534px}
  .page--back .brand__name{font-size:38px}
  .page--back .brand__sub{font-size:11px;letter-spacing:4.5px}

  .welcome{position:absolute;right:32px;top:650px;font-family:"Exo 2",sans-serif;font-weight:700;font-size:24px;white-space:nowrap}
  .welcome em{font-style:normal;color:var(--blue-bright)}
  .specialty{position:absolute;right:32px;top:692px;width:480px;text-align:right;font-family:"Exo 2",sans-serif;font-weight:600;font-size:11.2px;line-height:1.32}
  .specialty em{font-style:normal;color:var(--blue-bright)}

  .footer{position:absolute;left:0;bottom:0;width:100%;height:28px;background:var(--grey-bar);
    display:flex;align-items:center;justify-content:space-between;padding:0 32px 0 32px;font-size:9.8px;color:var(--white)}
  .footer span{display:flex;align-items:center;gap:6px}
  .footer .phone{font-weight:700;font-size:10.2px}
  .footer svg{width:11px;height:11px;fill:var(--blue-bright)}

  .about{position:absolute;left:240px;top:506px;width:267px}
  .about h2{font-family:"Exo 2",sans-serif;font-weight:400;font-size:10px;color:var(--blue-bright);margin-bottom:9px}
  .about h2 b{font-weight:700}
  .about p{font-size:7.3px;line-height:1.34;text-align:justify;color:var(--text-soft)}

  .clients{position:absolute;left:34px;top:650px;width:473px}
  .clients__title{display:flex;align-items:center;gap:4px;font-family:"Exo 2",sans-serif;font-weight:600;font-size:9.5px;color:var(--blue-bright);white-space:nowrap}
  .clients__title::before,.clients__title::after{content:"";height:1px;background:#6d7a8c;flex:1}
  .clients__title::before{flex:0 0 148px}
  .clients__row{display:flex;gap:6px;margin-top:6px}
  .client{flex:1;height:25px;background:var(--white);color:var(--navy);display:flex;align-items:center;justify-content:center;text-align:center;
    font-family:"PT Sans",sans-serif;font-weight:700;font-size:6.6px;line-height:1.05;padding:0 2px}
  .cta{position:absolute;left:0;width:100%;top:716px;text-align:center;font-family:"Exo 2",sans-serif;font-weight:600;font-size:11.5px;color:var(--blue-bright)}
  .cta b{color:var(--white);font-weight:600}
</style>
</head>
<body>
<div class="stage">

  <!-- Front page -->
  <section class="page page--front">
    <svg class="art" width="540" height="765" viewBox="0 0 540 765">
      <defs>
        <linearGradient id="heroTone" x1="0" y1="0" x2="1" y2="1">
          <stop offset="0" stop-color="#5b4630"/>
          <stop offset=".45" stop-color="#9a7a48"/>
          <stop offset=".7" stop-color="#e6d3a0"/>
          <stop offset="1" stop-color="#6b5234"/>
        </linearGradient>
        <linearGradient id="warmTone" x1="0" y1="0" x2="1" y2="1">
          <stop offset="0" stop-color="#3d3128"/><stop offset="1" stop-color="#a98a62"/>
        </linearGradient>
        <linearGradient id="lightTone" x1="0" y1="0" x2="1" y2="1">
          <stop offset="0" stop-color="#e8e6e2"/><stop offset="1" stop-color="#9f958a"/>
        </linearGradient>
        <linearGradient id="blueTone" x1="0" y1="0" x2="1" y2="1">
          <stop offset="0" stop-color="#22457a"/><stop offset="1" stop-color="#0f2346"/>
        </linearGradient>
        <linearGradient id="darkTone" x1="0" y1="0" x2="1" y2="1">
          <stop offset="0" stop-color="#2a2620"/><stop offset="1" stop-color="#8a7658"/>
        </linearGradient>
      </defs>

      <polygon points="0,0 540,0 540,232 0,360" fill="url(#heroTone)" role="img" aria-label="Project photo: The Silver Meadow Gaming Hall dining room with tufted booths and patterned carpet"/>

      <g transform="translate(-30,620) rotate(-28)">
        <rect x="-40" y="-330" width="760" height="350" fill="var(--navy-deep)" opacity=".92"/>
        <rect x="10" y="-150" width="150" height="140" fill="url(#lightTone)" stroke="#0a1326" stroke-width="6" role="img" aria-label="Project photo: long banquette dining row"/>
        <rect x="168" y="-150" width="150" height="140" fill="url(#lightTone)" stroke="#0a1326" stroke-width="6" role="img" aria-label="Project photo: food court booth seating"/>
        <rect x="326" y="-160" width="150" height="150" fill="url(#warmTone)" stroke="#0a1326" stroke-width="6" role="img" aria-label="Project photo: restaurant booths with pendant lights"/>
        <rect x="484" y="-170" width="170" height="160" fill="url(#lightTone)" stroke="#0a1326" stroke-width="6" role="img" aria-label="Project photo: bar seating beside a wood wall"/>
        <rect x="-30" y="-300" width="150" height="140" fill="url(#blueTone)" stroke="#0a1326" stroke-width="6" role="img" aria-label="Project photo: Dunmore Hall lounge with blue curved seating"/>
        <rect x="560" y="-320" width="160" height="140" fill="url(#darkTone)" stroke="#0a1326" stroke-width="6" role="img" aria-label="Project photo: dark lounge booth seating"/>
        <rect x="150" y="-255" width="56" height="56" fill="var(--blue)"/>
        <rect x="520" y="-15" width="56" height="56" fill="var(--blue)"/>
        <line x1="-20" y1="20" x2="700" y2="20" stroke="var(--blue)" stroke-width="1"/>
        <line x1="100" y1="-300" x2="700" y2="-300" stroke="var(--blue)" stroke-width="1"/>
      </g>
      <circle cx="97" cy="705" r="2" fill="var(--blue)"/>
      <circle cx="48" cy="393" r="2" fill="var(--blue)"/>
    </svg>

    <div class="brand"><span class="brand__name">Larkfield</span><span class="brand__sub">UPHOLSTERY</span></div>
    <h1 class="welcome">Welcome to <em>LARKFIELD UPHOLSTERY</em></h1>
    <p class="specialty">We specialize in <em>Custom Upholstery Work</em> on booths, banquettes, chairs &amp; other furniture<br>for restaurants, bars, cafes, medical offices, schools, condo buildings, etc.</p>

    <footer class="footer">
      <span><svg viewBox="0 0 12 12"><path d="M6 1 1 5.5h1.5V11h2.8V7.8h1.4V11h2.8V5.5H11z"/></svg>4812 Pemberly Rd. Edmonton, AB. T0X 9Z9</span>
      <span><svg viewBox="0 0 12 12"><circle cx="6" cy="6" r="5" fill="none" stroke="#2aa4ee" stroke-width="1.2"/><path d="M1 6h10M6 1c-2.5 3-2.5 7 0 10M6 1c2.5 3 2.5 7 0 10" fill="none" stroke="#2aa4ee" stroke-width="1"/></svg>www.larkfieldupholstery.example</span>
      <span class="phone"><svg viewBox="0 0 12 12"><path d="M2.5 1h2l1 3-1.3 1a6.5 6.5 0 0 0 2.8 2.8l1-1.3 3 1v2c0 .8-.7 1.5-1.5 1.5A9.5 9.5 0 0 1 1 2.5C1 1.7 1.7 1 2.5 1z"/></svg>780-555-0147</span>
    </footer>
  </section>

  <!-- Back page -->
  <section class="page page--back">
    <svg class="art" width="540" height="765" viewBox="0 0 540 765">
      <defs>
        <linearGradient id="g1" x1="0" y1="0" x2="1" y2="1"><stop offset="0" stop-color="#5a4430"/><stop offset=".6" stop-color="#2c3d55"/><stop offset="1" stop-color="#9a7a50"/></linearGradient>
        <linearGradient id="g2" x1="0" y1="0" x2="1" y2="1"><stop offset="0" stop-color="#a04a25"/><stop offset="1" stop-color="#e3ddd4"/></linearGradient>
        <linearGradient id="g3" x1="0" y1="0" x2="1" y2="1"><stop offset="0" stop-color="#d9c9b0"/><stop offset="1" stop-color="#a63a55"/></linearGradient>
        <linearGradient id="g4" x1="0" y1="0" x2="1" y2="1"><stop offset="0" stop-color="#3a2c22"/><stop offset="1" stop-color="#8e6a48"/></linearGradient>
        <linearGradient id="g5" x1="0" y1="0" x2="1" y2="1"><stop offset="0" stop-color="#b79a72"/><stop offset="1" stop-color="#e9ecef"/></linearGradient>
        <linearGradient id="g6" x1="0" y1="0" x2="1" y2="1"><stop offset="0" stop-color="#a33a22"/><stop offset="1" stop-color="#6a4026"/></linearGradient>
      </defs>
      <line x1="28" y1="26" x2="507" y2="26" stroke="var(--blue)" stroke-width="1.2"/>
      <circle cx="28" cy="26" r="2" fill="var(--blue)"/>
      <g stroke="#8f9aa8" stroke-width="1.5">
        <rect x="34" y="34" width="310" height="279" fill="url(#g1)" role="img" aria-label="Project photo: restaurant with blue tufted booths and pendant lights"/>
        <rect x="358" y="34" width="150" height="132" fill="url(#g2)" role="img" aria-label="Project photo: white booth rows along a corridor"/>
        <rect x="358" y="181" width="150" height="133" fill="url(#g3)" role="img" aria-label="Project photo: pink banquette beneath a wall mural"/>
        <rect x="34" y="327" width="150" height="132" fill="url(#g4)" role="img" aria-label="Project photo: leather booths below framed records"/>
        <rect x="196" y="327" width="150" height="132" fill="url(#g5)" role="img" aria-label="Project photo: bright dining room with wood slat ceiling"/>
        <rect x="358" y="327" width="150" height="132" fill="url(#g6)" role="img" aria-label="Project photo: rustic dining room with wooden tables"/>
      </g>
      <line x1="34" y1="471" x2="513" y2="471" stroke="var(--blue)" stroke-width="1.2"/>
      <circle cx="513" cy="471" r="2" fill="var(--blue)"/>
    </svg>

    <div class="brand"><span class="brand__name">Larkfield</span><span class="brand__sub">UPHOLSTERY</span></div>

    <div class="about">
      <h2><b>ABOUT</b> LARKFIELD UPHOLSTERY</h2>
      <p>Larkfield Upholstery has been serving North America for over 60 years. The company began as a family owned and operated business and has grown into a complete manufacturing facility. We can carry your vision straight through the manufacturing process, from initial drawings to finished product, including foam, fabric, framework, and associated millwork. Our 25,000 square foot facility has computer controlled cutters for both fabric and wood cutting capabilities. We have the capacity to take an original design and create products to meet your specifications, or adapt our standardized designs to fit your vision. We have a library of standard configurations that are customizable to meet almost any requirements.</p>
    </div>

    <div class="clients">
      <div class="clients__title">We have worked with These clients</div>
      <div class="clients__row">
        <div class="client">Dunmore Hall</div>
        <div class="client">Riverton City</div>
        <div class="client">Tovins</div>
        <div class="client">Harbin Crust</div>
        <div class="client">QWUK</div>
        <div class="client">Westvale Province</div>
        <div class="client">Corner Hanks</div>
        <div class="client">Northgate Plaza</div>
        <div class="client">Kestrel Ridge College</div>
      </div>
    </div>

    <p class="cta">FOR MORE DETAILS <b>CONTACT US</b> TODAY !</p>

    <footer class="footer">
      <span><svg viewBox="0 0 12 12"><path d="M6 1 1 5.5h1.5V11h2.8V7.8h1.4V11h2.8V5.5H11z"/></svg>4812 Pemberly Rd. Edmonton, AB. T0X 9Z9</span>
      <span><svg viewBox="0 0 12 12"><circle cx="6" cy="6" r="5" fill="none" stroke="#2aa4ee" stroke-width="1.2"/><path d="M1 6h10M6 1c-2.5 3-2.5 7 0 10M6 1c2.5 3 2.5 7 0 10" fill="none" stroke="#2aa4ee" stroke-width="1"/></svg>www.larkfieldupholstery.example</span>
      <span class="phone"><svg viewBox="0 0 12 12"><path d="M2.5 1h2l1 3-1.3 1a6.5 6.5 0 0 0 2.8 2.8l1-1.3 3 1v2c0 .8-.7 1.5-1.5 1.5A9.5 9.5 0 0 1 1 2.5C1 1.7 1.7 1 2.5 1z"/></svg>780-555-0147</span>
    </footer>
  </section>

</div>
</body>
</html>
```